Brightpagekit.com Website Design

We would like to redesign brightpagkit.com and we are looking for creative ideas. The new design should be clean and not resemble with any other existing website design.

The most important factor is that website have many banners/advertisements so the new design should be able to accommodate these banners of different size (Advertisement Friendly Design)

All Tools should be categorized under different main categories like all those tools that are related to content/writing will be shown under Content Tools ( Please find all categories and tools in attached file with the project). Right now all tools are showing randomly.

Also, Design single tool pages with sidebar, advertisement, and content placement.
ex. brightpagekit.com/plagiarism-checker/
brightpagekit.com/keyword-position/

Winning designer will also make the logo as well.

Target Market(s)

SEO Agencies, SEO executive, Article writers, Essay Writers, Plagiarism Checkers, Webmasters

Industry/Entity Type

Seo

Logo Text

Bright Page Kit

Number of Pages Required

5+ page

Font styles to use
Serif
Sans Serif
Other font styles liked:
• Any

Colors

Designer to choose colors to be used in the design.

Requirements
Must have
• 1) Clean Design
• 2) Modern Look
• 3) Easy To Navigate
• 4) Separate Icon for every Tool
• 5) Advertisement/Banners Freindly Design
Nice to have
• Matching Logo
• WOW Factor
Should not have
• Complex Design
• No drop down menu

```html
<!DOCTYPE html>
<html lang="en">
<head>
<meta charset="utf-8">
<title>Bright Page Kit</title>
<link href="https://fonts.googleapis.com/css2?family=Open+Sans:wght@400;600;700;800&display=swap" rel="stylesheet">
<style>
:root{
  --red:#e5232b;
  --red-dark:#b8141b;
  --ink:#1b1b1b;
  --text:#555;
  --muted:#888;
  --line:#dedede;
  --panel:#f3f3f3;
  --ad:#d9d9d9;
  --white:#fff;
  --hero-a:#3b3d42;
  --hero-b:#7a7c80;
}
*{box-sizing:border-box;margin:0;padding:0}
html,body{width:1200px;height:3408px;overflow:hidden}
body{font-family:"Open Sans",Arial,sans-serif;color:var(--ink);background:var(--white);position:relative}
.brand{display:flex;align-items:center;gap:10px;font-weight:700;font-size:22px;color:var(--white)}
.brand-dot{width:18px;height:18px;border-radius:50%;background:var(--red)}

/* hero */
.hero{position:relative;height:600px;overflow:hidden}
.hero-photo{position:absolute;inset:0;background:linear-gradient(110deg,var(--hero-a) 0%,#55575c 45%,var(--hero-b) 75%,#b9babd 100%)}
.hero-shade{position:absolute;inset:0;background:linear-gradient(90deg,rgba(20,20,22,.75) 0%,rgba(20,20,22,.35) 60%,rgba(20,20,22,.1) 100%)}
.topbar{position:absolute;top:22px;left:120px;right:80px;display:flex;justify-content:space-between;align-items:center}
.nav{background:var(--white);display:flex;gap:6px;padding:10px 14px}
.nav a{font-size:12px;font-weight:700;color:var(--ink);text-decoration:none;padding:6px 14px}
.nav a.active{color:var(--red);border:1px solid var(--red)}
.hero-copy{position:absolute;left:132px;top:170px;width:440px;color:var(--white)}
.hero-copy .pre{font-size:34px;font-weight:600;letter-spacing:.5px}
.hero-copy h1{font-size:50px;font-weight:800;color:var(--red);line-height:1.1}
.hero-copy p{font-size:16px;line-height:1.5;margin-top:22px;color:#eee}
.btn{display:inline-block;background:var(--red);color:var(--white);font-size:13px;font-weight:700;padding:12px 26px;text-transform:uppercase}
.hero-copy .btn{margin-top:30px}

/* about */
.about{height:620px;text-align:center;padding-top:80px}
.section-title{font-size:34px;font-weight:800;letter-spacing:1px}
.section-title:after{content:"";display:block;width:60px;height:4px;background:var(--red);margin:12px auto 0}
.about .lead{width:660px;margin:30px auto 0;font-size:16px;line-height:1.6;color:var(--text)}
.features{display:flex;justify-content:center;gap:100px;margin-top:60px}
.feature{width:230px}
.feature-icon{width:100px;height:100px;border:3px solid var(--red);border-radius:50%;margin:0 auto;display:flex;align-items:center;justify-content:center}
.feature h3{font-size:20px;font-weight:700;margin-top:20px;line-height:1.25}
.feature p{font-size:14px;color:var(--text);margin-top:10px;line-height:1.4}
.feature .btn{font-size:11px;padding:7px 14px;margin-top:16px;text-transform:none}

/* main */
.main{display:flex;gap:48px;padding:20px 140px 0;height:1740px}
.content{width:592px}
.ad{background:var(--ad);display:flex;align-items:center;justify-content:center;font-size:14px;font-weight:600;color:#444;text-transform:uppercase}
.ad-top{height:68px}
.cat{margin-top:20px;border:1px solid var(--line)}
.cat-head{background:var(--red);height:32px;display:flex;justify-content:space-between;align-items:center;padding:0 8px 0 12px;color:var(--white);font-size:13px;font-weight:700}
.arrows{display:flex;gap:4px}
.arrows span{width:22px;height:22px;background:var(--white);display:flex;align-items:center;justify-content:center}
.tools{display:flex;padding:20px 6px 18px}
.tool{width:25%;text-align:center;font-size:12px;font-weight:600;color:#333;line-height:1.3}
.tool svg{display:block;margin:0 auto 12px}
.load-more{text-align:center;margin-top:36px}
.ad-wide{height:72px;margin-top:44px}
.ad-pair{display:flex;gap:32px;margin-top:36px;padding:0 0}
.ad-pair .ad{flex:1;height:204px}

.sidebar{width:280px}
.widget{border:1px solid var(--line)}
.widget-head{background:var(--red);color:var(--white);font-size:13px;font-weight:700;padding:8px 12px}
.search-body{padding:18px 12px}
.search-input{border:1px solid var(--line);height:36px;font-size:12px;color:var(--muted);display:flex;align-items:center;padding-left:10px}
.search-btn{margin-top:12px;background:var(--ink);color:var(--white);text-align:center;font-size:13px;font-weight:700;padding:10px}
.ad-side{height:180px;margin-top:20px}
.popular{margin-top:40px}
.pop-list{list-style:none;padding:4px 12px}
.pop-list li{display:flex;align-items:center;gap:14px;height:52px;border-bottom:1px solid #eee;font-size:14px;color:#333}
.pop-list li:last-child{border-bottom:none}
.pop-list li.hot{color:var(--red);font-weight:600}
.pop-ico{width:26px;height:26px;background:var(--ink);flex:none}
.ad-side2{height:160px;margin-top:0}
.follow{margin-top:40px}
.follow-body{display:flex;justify-content:center;gap:24px;padding:24px 0}
.circle{width:56px;height:56px;border-radius:50%}

/* footer */
.footer{position:absolute;left:0;top:2960px;width:1200px;height:448px;background:linear-gradient(160deg,#f12a31 0%,var(--red) 50%,var(--red-dark) 100%);color:var(--white)}
.footer-cols{display:flex;padding:80px 120px 0}
.f-brand{width:400px}
.f-brand .brand{font-size:24px}
.f-brand .brand-dot{background:var(--white)}
.f-info{margin-top:34px;font-size:12px;line-height:1.7}
.f-info div{display:flex;gap:12px;margin-bottom:12px;align-items:flex-start}
.f-info svg{flex:none;margin-top:3px}
.f-links{width:240px}
.f-links h4,.f-news h4{font-size:16px;font-weight:700;margin-bottom:22px}
.f-links li{list-style:none;font-size:13px;margin-bottom:14px;padding-left:16px;position:relative}
.f-links li:before{content:"";position:absolute;left:0;top:6px;width:6px;height:6px;background:var(--white)}
.f-news{width:320px}
.f-news p{font-size:13px;line-height:1.5}
.f-input{margin-top:18px;border:1px solid rgba(255,255,255,.7);height:38px;font-size:12px;display:flex;align-items:center;padding-left:12px}
.f-btn{display:inline-block;margin-top:14px;background:var(--ink);color:var(--white);font-size:12px;font-weight:700;padding:10px 22px}
.f-bottom{position:absolute;left:120px;right:120px;bottom:0;height:60px;border-top:1px solid rgba(255,255,255,.35);display:flex;justify-content:space-between;align-items:center;font-size:12px}
.f-social{display:flex;gap:12px}
.f-social span{width:26px;height:26px;border-radius:50%;background:var(--white)}
</style>
</head>
<body>

<header class="hero">
  <div class="hero-photo" role="img" aria-label="Photo of a desk with a laptop, tablet and mouse"></div>
  <div class="hero-shade"></div>
  <div class="topbar">
    <div class="brand"><span class="brand-dot"></span>Bright Page Kit</div>
    <nav class="nav">
      <a class="active">HOME</a><a>SERVICES</a><a>TOOLS</a><a>ADVERTISE</a><a>BLOG</a><a>CONTACT</a><a>LOGIN</a>
    </nav>
  </div>
  <div class="hero-copy">
    <div class="pre">LARGEST PLATFORM FOR</div>
    <h1>BEST SEO TOOLS</h1>
    <p>Sed ut perspiciatis unde omnis iste natus error sit voluptatem accusantium doloremque laudantium, totam rem.</p>
    <span class="btn">Take Tour</span>
  </div>
</header>

<section class="about">
  <h2 class="section-title">ABOUT US</h2>
  <p class="lead">Sed ut perspiciatis unde omnis iste natus error sit voluptatem accusan- tium doloremque laudantium, totam rem aperiam</p>
  <div class="features">
    <div class="feature">
      <div class="feature-icon"><svg width="50" height="50" viewBox="0 0 50 50"><path d="M30 8 L42 8 L42 20 L26 36 L14 24 Z" fill="#1b1b1b"/><circle cx="34" cy="16" r="3" fill="#fff"/><path d="M14 30 L8 42 L20 36 Z" fill="#e5232b"/></svg></div>
      <h3>Largest SEO Tools Collection</h3>
      <p>architecto beatae vitae dicta sunt explicabo. Nemo enim ipsam</p>
      <span class="btn">Learn more</span>
    </div>
    <div class="feature">
      <div class="feature-icon"><svg width="50" height="50" viewBox="0 0 50 50"><rect x="10" y="30" width="30" height="12" fill="#1b1b1b"/><path d="M16 30 L22 10 L28 10 L34 30 Z" fill="#1b1b1b"/><rect x="22" y="16" width="6" height="10" fill="#fff"/></svg></div>
      <h3>Best SEO Tool Kit Available</h3>
      <p>architecto beatae vitae dicta sunt explicabo. Nemo enim ipsam</p>
      <span class="btn">Learn more</span>
    </div>
    <div class="feature">
      <div class="feature-icon"><svg width="50" height="50" viewBox="0 0 50 50"><rect x="8" y="32" width="7" height="10" fill="#1b1b1b"/><rect x="19" y="26" width="7" height="16" fill="#1b1b1b"/><rect x="30" y="18" width="7" height="24" fill="#1b1b1b"/><path d="M8 24 L22 14 L30 18 L42 8" stroke="#e5232b" stroke-width="3" fill="none"/></svg></div>
      <h3>Make Your Site Boost</h3>
      <p>architecto beatae vitae dicta sunt explicabo. Nemo enim ipsam</p>
      <span class="btn">Learn more</span>
    </div>
  </div>
</section>

<main class="main">
  <div class="content">
    <div class="ad ad-top">Advertisement</div>

    <div class="cat">
      <div class="cat-head">CONTENT TOOLS<div class="arrows"><span><svg width="8" height="10"><path d="M7 1 L2 5 L7 9" stroke="#e5232b" stroke-width="2" fill="none"/></svg></span><span><svg width="8" height="10"><path d="M1 1 L6 5 L1 9" stroke="#e5232b" stroke-width="2" fill="none"/></svg></span></div></div>
      <div class="tools">
        <div class="tool"><svg width="44" height="44"><rect x="8" y="4" width="24" height="30" fill="#1b1b1b"/><rect x="14" y="10" width="24" height="30" fill="#1b1b1b" stroke="#fff" stroke-width="2"/></svg>Plagiarism Checker</div>
        <div class="tool"><svg width="44" height="44"><circle cx="22" cy="22" r="18" fill="#1b1b1b"/><path d="M14 22 L22 14 L30 22 L22 30 Z" fill="#fff"/></svg>Article Rewriter</div>
        <div class="tool"><svg width="44" height="44"><rect x="4" y="4" width="36" height="36" fill="#1b1b1b"/><path d="M12 34 L22 10 L32 34 M16 26 H28" stroke="#fff" stroke-width="3" fill="none"/></svg>Grammar Checker</div>
        <div class="tool"><svg width="44" height="44"><rect x="6" y="4" width="32" height="36" fill="#1b1b1b"/><path d="M12 14 H32 M12 22 H32 M12 30 H24" stroke="#fff" stroke-width="2"/></svg>Word Count Checker</div>
      </div>
    </div>

    <div class="cat">
      <div class="cat-head">IMAGE HANDLING<div class="arrows"><span><svg width="8" height="10"><path d="M7 1 L2 5 L7 9" stroke="#e5232b" stroke-width="2" fill="none"/></svg></span><span><svg width="8" height="10"><path d="M1 1 L6 5 L1 9" stroke="#e5232b" stroke-width="2" fill="none"/></svg></span></div></div>
      <div class="tools">
        <div class="tool"><svg width="44" height="44"><rect x="4" y="6" width="36" height="32" fill="#1b1b1b"/><path d="M8 32 L18 20 L26 28 L30 24 L36 32 Z" fill="#fff"/><circle cx="30" cy="14" r="3" fill="#fff"/></svg>Reverse Image Search</div>
        <div class="tool"><svg width="44" height="44"><rect x="6" y="6" width="14" height="32" fill="#1b1b1b"/><rect x="24" y="14" width="14" height="24" fill="#1b1b1b"/><path d="M10 14 H16 M10 20 H16" stroke="#fff" stroke-width="2"/></svg>Image Compression</div>
        <div class="tool"><svg width="44" height="44"><rect x="4" y="6" width="36" height="32" fill="#1b1b1b"/><path d="M12 16 H32 M12 22 H32 M12 28 H32" stroke="#fff" stroke-width="2"/></svg>Favicon Generator</div>
        <div class="tool"><svg width="44" height="44"><rect x="4" y="8" width="26" height="28" fill="#1b1b1b"/><path d="M30 16 L40 10 V34 L30 28 Z" fill="#1b1b1b"/></svg>Video to gif Converter</div>
      </div>
    </div>

    <div class="cat">
      <div class="cat-head">KEYWORD TOOLS<div class="arrows"><span><svg width="8" height="10"><path d="M7 1 L2 5 L7 9" stroke="#e5232b" stroke-width="2" fill="none"/></svg></span><span><svg width="8" height="10"><path d="M1 1 L6 5 L1 9" stroke="#e5232b" stroke-width="2" fill="none"/></svg></span></div></div>
      <div class="tools">
        <div class="tool"><svg width="44" height="44"><path d="M4 38 H40 M4 38 V6" stroke="#1b1b1b" stroke-width="3"/><path d="M8 32 L18 20 L26 26 L38 10" stroke="#1b1b1b" stroke-width="4" fill="none"/></svg>Keyword Position</div>
        <div class="tool"><svg width="44" height="44"><rect x="10" y="4" width="24" height="36" fill="#1b1b1b"/><path d="M16 12 H28 M16 20 H28 M16 28 H28" stroke="#fff" stroke-width="2"/></svg>Keywords Density Checker</div>
        <div class="tool"><svg width="44" height="44"><circle cx="22" cy="22" r="18" fill="#1b1b1b"/><path d="M16 17 Q16 11 22 11 Q28 11 28 17 Q28 21 22 23 V27" stroke="#fff" stroke-width="3" fill="none"/><circle cx="22" cy="32" r="2" fill="#fff"/></svg>Keywords Suggestion Tool</div>
        <div class="tool"><svg width="44" height="44"><rect x="4" y="8" width="36" height="28" fill="#1b1b1b"/><path d="M10 16 H34 M10 22 H34 M10 28 H26" stroke="#fff" stroke-width="2"/></svg>Website Keyword Suggestion tool</div>
      </div>
    </div>

    <div class="cat">
      <div class="cat-head">BACKLINK TOOLS<div class="arrows"><span><svg width="8" height="10"><path d="M7 1 L2 5 L7 9" stroke="#e5232b" stroke-width="2" fill="none"/></svg></span><span><svg width="8" height="10"><path d="M1 1 L6 5 L1 9" stroke="#e5232b" stroke-width="2" fill="none"/></svg></span></div></div>
      <div class="tools">
        <div class="tool"><svg width="44" height="44"><rect x="6" y="14" width="18" height="10" rx="5" fill="none" stroke="#1b1b1b" stroke-width="4" transform="rotate(-45 15 19)"/><rect x="20" y="20" width="18" height="10" rx="5" fill="none" stroke="#1b1b1b" stroke-width="4" transform="rotate(-45 29 25)"/></svg>Backlink Checker</div>
        <div class="tool"><svg width="44" height="44"><rect x="14" y="4" width="14" height="10" rx="5" fill="none" stroke="#1b1b1b" stroke-width="4"/><rect x="14" y="17" width="14" height="10" rx="5" fill="none" stroke="#1b1b1b" stroke-width="4"/><rect x="14" y="30" width="14" height="10" rx="5" fill="none" stroke="#1b1b1b" stroke-width="4"/></svg>Backlink Maker</div>
        <div class="tool"><svg width="44" height="44"><rect x="6" y="4" width="32" height="36" fill="#1b1b1b"/><path d="M12 14 H32 M12 22 H32 M12 30 H32" stroke="#fff" stroke-width="2"/></svg>Website Link Count Checker</div>
        <div class="tool"><svg width="44" height="44"><rect x="4" y="10" width="18" height="10" rx="5" fill="none" stroke="#1b1b1b" stroke-width="4"/><rect x="22" y="24" width="18" height="10" rx="5" fill="none" stroke="#1b1b1b" stroke-width="4"/><path d="M20 26 L24 18" stroke="#e5232b" stroke-width="3"/></svg>Website Broken Link Checker</div>
      </div>
    </div>

    <div class="cat">
      <div class="cat-head">WEBSITE TOOLS<div class="arrows"><span><svg width="8" height="10"><path d="M7 1 L2 5 L7 9" stroke="#e5232b" stroke-width="2" fill="none"/></svg></span><span><svg width="8" height="10"><path d="M1 1 L6 5 L1 9" stroke="#e5232b" stroke-width="2" fill="none"/></svg></span></div></div>
      <div class="tools">
        <div class="tool"><svg width="44" height="44"><rect x="4" y="6" width="36" height="26" fill="#1b1b1b"/><rect x="16" y="32" width="12" height="6" fill="#1b1b1b"/><rect x="10" y="38" width="24" height="3" fill="#1b1b1b"/></svg>Website Seo Score Checker</div>
        <div class="tool"><svg width="44" height="44"><text x="22" y="32" text-anchor="middle" font-family="Open Sans, sans-serif" font-weight="800" font-style="italic" font-size="26" fill="#1b1b1b">PR</text></svg>Page Rank Checker</div>
        <div class="tool"><svg width="44" height="44"><circle cx="10" cy="34" r="5" fill="#1b1b1b"/><path d="M6 20 A18 18 0 0 1 24 38 M6 8 A30 30 0 0 1 36 38" stroke="#1b1b1b" stroke-width="5" fill="none"/></svg>Online Ping Website Tool</div>
        <div class="tool"><svg width="44" height="44"><rect x="4" y="4" width="36" height="36" rx="6" fill="#1b1b1b"/><path d="M12 30 A12 12 0 0 1 32 30" stroke="#fff" stroke-width="3" fill="none"/><path d="M22 30 L28 18" stroke="#fff" stroke-width="3"/></svg>Website Page Speed Checker</div>
      </div>
    </div>

    <div class="load-more"><span class="btn" style="text-transform:none">Load More Tools</span></div>
    <div class="ad ad-wide">Advertisement</div>
    <div class="ad-pair"><div class="ad">Advertisement</div><div class="ad">Advertisement</div></div>
  </div>

  <aside class="sidebar">
    <div class="widget">
      <div class="widget-head">SEARCH TOOLS</div>
      <div class="search-body">
        <div class="search-input">Search from 600 Tools</div>
        <div class="search-btn">SEARCH</div>
      </div>
    </div>
    <div class="ad ad-side">Advertisement</div>
    <div class="widget popular">
      <div class="widget-head">POPULAR TOOLS</div>
      <ul class="pop-list">
        <li><span class="pop-ico"></span>Plagiarism Checker</li>
        <li><span class="pop-ico"></span>Article Rewriter</li>
        <li><span class="pop-ico"></span>Grammar Checker</li>
        <li><span class="pop-ico"></span>Word Count Checker</li>
        <li><span class="pop-ico"></span>Reverse Image Search</li>
        <li><span class="pop-ico"></span>Image Compression</li>
        <li><span class="pop-ico"></span>Video To Gif Converter</li>
        <li><span class="pop-ico"></span>Plagiarism Checker</li>
        <li><span class="pop-ico"></span>Article Rewriter</li>
        <li><span class="pop-ico"></span>Grammar Checker</li>
        <li><span class="pop-ico"></span>Word Count Checker</li>
        <li><span class="pop-ico"></span>Reverse Image Search</li>
        <li><span class="pop-ico"></span>Image Compression</li>
        <li><span class="pop-ico"></span>Video To Gif Converter</li>
        <li class="hot"><span class="pop-ico"></span>Keyword Position</li>
      </ul>
    </div>
    <div class="ad ad-side2">Advertisement</div>
    <div class="widget follow">
      <div class="widget-head">FOLLOW US</div>
      <div class="follow-body">
        <span class="circle" style="background:#3b5998" aria-label="Social profile"></span>
        <span class="circle" style="background:#2fa9e0" aria-label="Social profile"></span>
        <span class="circle" style="background:#db4437" aria-label="Social profile"></span>
      </div>
    </div>
  </aside>
</main>

<footer class="footer">
  <div class="footer-cols">
    <div class="f-brand">
      <div class="brand"><span class="brand-dot"></span>Bright Page Kit</div>
      <div class="f-info">
        <div><svg width="12" height="16"><path d="M6 1 A5 5 0 0 1 11 6 C11 10 6 15 6 15 C6 15 1 10 1 6 A5 5 0 0 1 6 1 Z" fill="#fff"/></svg><span>214 Marlow Lane, 9th Orchard Road,<br>Easton</span></div>
        <div><svg width="12" height="16"><rect x="2" y="1" width="8" height="14" rx="2" fill="#fff"/></svg><span>555 014 782<br>555 019 4420</span></div>
        <div><svg width="14" height="12"><rect x="0" y="1" width="14" height="10" fill="#fff"/><path d="M0 1 L7 7 L14 1" stroke="#e5232b" fill="none"/></svg><span>info@brightpagekit.com</span></div>
      </div>
    </div>
    <div class="f-links">
      <h4>Quick Links</h4>
      <ul><li>Terms of Services</li><li>Testimonials</li><li>Privacy Policy</li><li>Contact Us</li></ul>
    </div>
    <div class="f-news">
      <h4>Subscribe to Our Newsletter</h4>
      <p>Sed ut perspiciatis unde omnis iste natus error sit voluptatem accusantium doloremque</p>
      <div class="f-input">Enter Your Email</div>
      <span class="f-btn">SUBSCRIBE</span>
    </div>
  </div>
  <div class="f-bottom">
    <span>Copyright © 2012-2017 by BrightPageKit.com - All Rights Reserved</span>
    <div class="f-social"><span></span><span></span><span></span><span></span></div>
  </div>
</footer>

</body>
</html>
```